Local Computer Repair Business needs Flyer Design

I am looking for a small postcard sized (4x6) advertisement but use the full space 4x6. We are a local computer repair shop that provide sales and service of computer systems, any models, any problems. We also offer E-cycling for our customers. This will be distributed via post office box.
Emphasize shop locally, best service around, professional, Competitive prices.
One side for computer sales/repair and the other side should be E-Cycling. we'll receive old laptops, desktop computers, tablets, game consoles, etc..
Ad must include the attached logo.
Ad must include address - 872 Larkspur Ave. Hudson, IA 50619
Ad must include phone number and website - 319-555-0174 and www.quillbyrnservices.com

```html
<!DOCTYPE html>
<html lang="en">
<head>
<meta charset="utf-8">
<title>Quillbyrn Services Postcard</title>
<link rel="stylesheet" href="https://fonts.googleapis.com/css2?family=Arimo:wght@400;700&family=Oswald:wght@500&display=swap">
<style>
  :root {
    --red: #e31e24;
    --blue: #1b8ad3;
    --navy: #1b3d8f;
    --gray: #7d7d7d;
    --dark: #2b2b2b;
    --ink: #222;
    --light: #e6e6e6;
    --bg: #efefef;
  }
  * { margin: 0; padding: 0; box-sizing: border-box; }
  html, body { width: 1200px; height: 1200px; overflow: hidden; background: var(--bg); }
  body { font-family: "Arimo", Arial, sans-serif; color: var(--ink); position: relative; }
  .card {
    position: absolute; left: 180px; width: 840px; height: 558px;
    background: #fff; overflow: hidden; box-shadow: 0 4px 14px rgba(0,0,0,.25);
  }
  .card--front { top: 28px; }
  .card--back { top: 614px; }
  .card-shapes { position: absolute; inset: 0; width: 840px; height: 558px; }
  .abs { position: absolute; }
  .condensed { font-family: "Oswald", "Arial Narrow", sans-serif; font-weight: 500; text-transform: uppercase; }

  /* front */
  .ecycle-title { left: 78px; top: 12px; font-size: 46px; color: #fff; line-height: 1.1; }
  .ecycle-text { left: 18px; top: 80px; width: 300px; font-size: 10.5px; line-height: 1.3; color: #fff; }
  .data-title { left: 18px; top: 220px; font-size: 14.5px; color: var(--ink); }
  .data-text { left: 18px; top: 248px; width: 310px; font-size: 9.6px; line-height: 1.3; text-align: justify; }
  .tagline { left: 390px; top: 14px; font-size: 30px; line-height: 1.35; color: var(--navy); }
  .tagline .bar { color: var(--red); }
  .receive { left: 22px; top: 374px; font-size: 25px; color: #fff; line-height: 1; letter-spacing: -.2px; }
  .brand { left: 26px; top: 462px; display: flex; align-items: center; gap: 12px; }
  .brand-dot { width: 34px; height: 34px; border-radius: 50%; background: var(--red); }
  .brand-name { font-weight: 700; font-size: 25px; color: var(--navy); letter-spacing: 1px; line-height: 1.05; }

  /* contact */
  .contact { color: #fff; font-size: 18px; line-height: 1; }
  .contact li { list-style: none; display: flex; align-items: center; gap: 10px; height: 27px; }
  .contact svg { width: 15px; height: 15px; flex: none; }
  .contact--front { left: 462px; top: 454px; }
  .contact--back { left: 18px; top: 464px; font-size: 17px; }

  /* back */
  .service { width: 230px; }
  .service-head { display: flex; gap: 10px; align-items: flex-start; }
  .service-icon { width: 38px; height: 38px; flex: none; }
  .service-title { color: var(--red); font-weight: 700; font-size: 12.6px; line-height: 1.2; padding-top: 8px; }
  .service-text { margin-left: 52px; margin-top: 4px; font-size: 10.5px; line-height: 1.22; text-align: justify; width: 162px; }
  .stamp { left: 738px; top: 16px; width: 78px; height: 94px; background: var(--light); }
</style>
</head>
<body>

<!-- E-Cycling side -->
<section class="card card--front">
  <svg class="card-shapes" viewBox="0 0 640 425" preserveAspectRatio="none" aria-hidden="true">
    <defs>
      <linearGradient id="photoTone" x1="0" y1="0" x2="0" y2="1">
        <stop offset="0" stop-color="#d9d9d9"/>
        <stop offset=".55" stop-color="#9a9a9a"/>
        <stop offset="1" stop-color="#c4c4c4"/>
      </linearGradient>
    </defs>
    <polygon points="322,72 640,72 640,278 262,278" fill="url(#photoTone)"/>
    <polygon points="0,0 262,0 298,150 0,150" fill="var(--blue)"/>
    <rect x="0" y="278" width="640" height="40" fill="var(--red)"/>
    <polygon points="340,330 640,330 640,412 300,412" fill="var(--gray)"/>
    <polygon points="330,330 342,330 302,412 290,412" fill="var(--dark)"/>
    <circle cx="30" cy="27" r="11" fill="none" stroke="var(--red)" stroke-width="5" stroke-dasharray="16 7"/>
  </svg>
  <div class="abs" role="img" aria-label="Photo of a laptop with a stethoscope on a wooden desk" style="left:420px;top:110px;width:1px;height:1px"></div>

  <h1 class="abs condensed ecycle-title">E-Cycling</h1>
  <p class="abs ecycle-text">Many people are unaware of the various hazardous substances that can be found in our everyday electronics. These hazardous and toxic materials become harmful to our health as well as the environment when not disposed of properly. Our E-Cycling process follows government guidelines to ensure safe disposal. So when it's time to replace your old or broken electronics, give us a call.</p>

  <h2 class="abs data-title">DATA DESTRUCTION (OPTIONAL)</h2>
  <p class="abs data-text">Quillbyrn Services does offer data destruction as part of our recycling process. This option does have a fee associated with it.<br>If you are interested in data destruction just let us know when you contact us for recycling.<br>If you have a business we do offer data destruction on-site, contact us for a quote.</p>

  <p class="abs condensed tagline">Shop Locally <span class="bar">|</span> Best Service Around <span class="bar">|</span><br>Professional <span class="bar">|</span> Competitive Prices</p>

  <p class="abs condensed receive">We'll receive old laptops, desktop computers, tablets, game consoles, etc..</p>

  <div class="abs brand">
    <span class="brand-dot"></span>
    <span class="brand-name">QUILLBYRN<br>SERVICES, LLC.</span>
  </div>

  <ul class="abs contact contact--front">
    <li><svg viewBox="0 0 16 16"><path d="M3 2h3l1 4-2 1c1 2 2 3 4 4l1-2 4 1v3c0 1-1 2-2 2C7 15 1 9 1 4c0-1 1-2 2-2z" fill="#fff"/></svg>319-555-0174</li>
    <li><svg viewBox="0 0 16 16"><circle cx="8" cy="8" r="6.5" fill="none" stroke="#fff" stroke-width="1.6"/><path d="M1.5 8h13M8 1.5c-3 3-3 10 0 13M8 1.5c3 3 3 10 0 13" fill="none" stroke="#fff" stroke-width="1.2"/></svg>www.quillbyrnservices.com</li>
    <li><svg viewBox="0 0 16 16"><path d="M8 1a5 5 0 0 1 5 5c0 4-5 9-5 9S3 10 3 6a5 5 0 0 1 5-5z" fill="#fff"/><circle cx="8" cy="6" r="2" fill="var(--gray)"/></svg>872 Larkspur Ave. Hudson, IA 50619</li>
  </ul>
</section>

<!-- Repair side -->
<section class="card card--back">
  <svg class="card-shapes" viewBox="0 0 640 425" preserveAspectRatio="none" aria-hidden="true">
    <polygon points="0,352 380,288 345,425 0,425" fill="var(--gray)"/>
    <polygon points="0,346 382,282 380,290 0,354" fill="var(--dark)"/>
    <polygon points="388,0 435,0 368,262 0,345 0,336 332,255" fill="var(--red)"/>
    <g stroke="#c9c9c9" stroke-width="1">
      <line x1="400" y1="182" x2="622" y2="182"/>
      <line x1="400" y1="205" x2="622" y2="205"/>
      <line x1="400" y1="230" x2="622" y2="230"/>
      <line x1="400" y1="260" x2="622" y2="260"/>
      <line x1="400" y1="288" x2="622" y2="288"/>
    </g>
  </svg>
  <div class="abs stamp"></div>

  <div class="abs service" style="left:16px;top:16px">
    <div class="service-head">
      <svg class="service-icon" viewBox="0 0 38 38"><circle cx="19" cy="19" r="17" fill="#fff" stroke="var(--blue)" stroke-width="2"/><path d="M12 26l9-9" stroke="var(--red)" stroke-width="4" stroke-linecap="round"/><circle cx="23" cy="15" r="5" fill="var(--red)"/></svg>
      <h3 class="service-title">REPAIRS/UPGRADES</h3>
    </div>
    <p class="service-text">Notebook, Laptop, PC, Computer repairs and upgrades. We can do any computer repair. Most repairs can be completed in 24/48 hrs</p>
  </div>

  <div class="abs service" style="left:16px;top:140px">
    <div class="service-head">
      <svg class="service-icon" viewBox="0 0 38 38"><circle cx="19" cy="19" r="17" fill="#fff" stroke="var(--blue)" stroke-width="2"/><rect x="10" y="12" width="18" height="12" fill="none" stroke="var(--red)" stroke-width="2"/><rect x="8" y="25" width="22" height="3" fill="var(--red)"/></svg>
      <h3 class="service-title">VIRUS AND MALWARE<br>REMOVAL</h3>
    </div>
    <p class="service-text">Our multi-scanning and detection process finds and eliminates viruses and</p>
  </div>

  <div class="abs service" style="left:16px;top:256px">
    <div class="service-head">
      <svg class="service-icon" viewBox="0 0 38 38"><circle cx="19" cy="19" r="17" fill="#fff" stroke="var(--blue)" stroke-width="2"/><path d="M19 9v9M15 14l4 4 4-4" fill="none" stroke="var(--red)" stroke-width="2"/><rect x="10" y="21" width="18" height="7" fill="var(--red)"/></svg>
      <h3 class="service-title">SOFTWARE INSTALLATIONS<br>AND CONFIGURATION</h3>
    </div>
    <p class="service-text">Is your software or equipment not installing? We can help you with the many ins and outs of making your software work for you.</p>
  </div>

  <div class="abs service" style="left:250px;top:18px">
    <div class="service-head">
      <svg class="service-icon" viewBox="0 0 38 38"><circle cx="19" cy="19" r="17" fill="#fff" stroke="var(--blue)" stroke-width="2"/><rect x="10" y="11" width="18" height="13" fill="none" stroke="var(--red)" stroke-width="2"/><path d="M15 28h8" stroke="var(--red)" stroke-width="2"/></svg>
      <h3 class="service-title">CUSTOM COMPUTERS</h3>
    </div>
    <p class="service-text">We build custom computers for gaming, entertainment or office use. Every computer is backed by our 1-year warranty for parts and labor. Satisfaction Guaranteed.</p>
  </div>

  <div class="abs service" style="left:250px;top:160px">
    <div class="service-head">
      <svg class="service-icon" viewBox="0 0 38 38"><circle cx="19" cy="19" r="17" fill="#fff" stroke="var(--blue)" stroke-width="2"/><rect x="10" y="11" width="18" height="12" fill="none" stroke="var(--red)" stroke-width="2"/><path d="M8 26h22" stroke="var(--red)" stroke-width="3"/></svg>
      <h3 class="service-title">LAPTOP SCREEN<br>REPAIR</h3>
    </div>
    <p class="service-text" style="text-align:left">Most damaged or broken laptop screens can be replaced for less than $150 Parts &amp; Labor.</p>
  </div>

  <ul class="abs contact contact--back">
    <li><svg viewBox="0 0 16 16"><path d="M3 2h3l1 4-2 1c1 2 2 3 4 4l1-2 4 1v3c0 1-1 2-2 2C7 15 1 9 1 4c0-1 1-2 2-2z" fill="#fff"/></svg>319-555-0174</li>
    <li><svg viewBox="0 0 16 16"><circle cx="8" cy="8" r="6.5" fill="none" stroke="#fff" stroke-width="1.6"/><path d="M1.5 8h13M8 1.5c-3 3-3 10 0 13M8 1.5c3 3 3 10 0 13" fill="none" stroke="#fff" stroke-width="1.2"/></svg>www.quillbyrnservices.com</li>
    <li><svg viewBox="0 0 16 16"><path d="M8 1a5 5 0 0 1 5 5c0 4-5 9-5 9S3 10 3 6a5 5 0 0 1 5-5z" fill="#fff"/><circle cx="8" cy="6" r="2" fill="var(--gray)"/></svg>872 Larkspur Ave. Hudson, IA 50619</li>
  </ul>
</section>

</body>
</html>
```